redesign of www.varqolo.com

Need redesign of our website to be more professionally looking. International import & export, warehousing and distribution business primarily from China to North America.

A few professional pictures needed on the new website.

Contact form also is needed.

Total 5 - 10 pages will be OK.

```html
<!DOCTYPE html>
<html lang="en">
<head>
<meta charset="utf-8">
<title>VARQOLO Inc — International Import &amp; Export</title>
<link rel="stylesheet" href="https://fonts.googleapis.com/css2?family=Oxygen:wght@300;400;700&family=Open+Sans:wght@300;400;600;700&display=swap">
<style>
  :root {
    --orange: #f29c12;
    --ink: #1f1f1f;
    --body-text: #555555;
    --rule: #e4e4e4;
    --nav-active: #f4f4f4;
    --footer-bg: #2e2e2e;
    --footer-text: #e8e8e8;
    --footer-muted: #b5b5b5;
    --white: #ffffff;
  }
  * { margin: 0; padding: 0; box-sizing: border-box; }
  html, body { width: 1200px; height: 920px; overflow: hidden; background: var(--white); }
  body { position: relative; font-family: "Open Sans", Arial, sans-serif; color: var(--ink); }

  .site-header { position: absolute; left: 0; top: 0; width: 1200px; height: 112px; background: var(--white); }
  .brand { position: absolute; left: 110px; top: 22px; height: 76px; display: flex; align-items: center; }
  .brand-mark { width: 22px; height: 22px; border-radius: 50%; background: var(--orange); margin-right: 10px; }
  .brand-name { font-family: "Oxygen", Arial, sans-serif; font-weight: 700; font-size: 34px; color: var(--ink); letter-spacing: 0.5px; }
  .brand-divider { width: 1px; height: 74px; background: #333; margin: 0 10px 0 16px; transform: rotate(4deg); }
  .brand-tagline { font-family: "Open Sans", Arial, sans-serif; font-style: italic; font-size: 10.5px; line-height: 13px; color: #222; }

  .main-nav { position: absolute; left: 534px; top: 0; height: 112px; display: flex; }
  .main-nav a {
    display: flex; align-items: flex-end; justify-content: center; padding-bottom: 30px;
    height: 112px; border-left: 1px solid var(--rule);
    font-family: "Oxygen", Arial, sans-serif; font-size: 16px; color: var(--ink); text-decoration: none;
  }
  .main-nav a.is-active { background: var(--nav-active); }
  .main-nav a:nth-child(1) { width: 91px; }
  .main-nav a:nth-child(2) { width: 119px; }
  .main-nav a:nth-child(3) { width: 116px; }
  .main-nav a:nth-child(4) { width: 113px; }
  .main-nav a:nth-child(5) { width: 112px; }

  .hero-band { position: absolute; left: 0; top: 112px; width: 1200px; height: 365px; background: var(--orange); }
  .hero-slide {
    position: absolute; left: 110px; top: 0; width: 975px; height: 365px;
    background: radial-gradient(ellipse at 30% 20%, #d9e8d4 0%, #c3cfc1 35%, #e9ece8 70%, #f3f3f3 100%);
  }
  .hero-title {
    position: absolute; left: 0; top: 140px; width: 975px; text-align: center;
    font-family: "Oxygen", Arial, sans-serif; font-weight: 700; font-size: 38px; line-height: 38px;
    color: var(--white); text-shadow: 0 2px 4px rgba(0,0,0,0.45);
  }
  .slide-dots { position: absolute; left: 462px; top: 345px; display: flex; gap: 4px; }
  .slide-dots span { width: 13px; height: 13px; border-radius: 50%; background: var(--white); }
  .slide-dots span.is-current { background: #000; }

  .welcome { position: absolute; left: 112px; top: 514px; width: 628px; }
  .welcome h1 { font-family: "Oxygen", Arial, sans-serif; font-weight: 400; font-size: 29px; color: var(--ink); margin-bottom: 11px; }
  .welcome h1 .light { font-weight: 300; }
  .welcome p { font-family: "Open Sans", Arial, sans-serif; font-weight: 300; font-size: 12.4px; line-height: 21px; color: var(--body-text); }

  .feature-photo { position: absolute; left: 758px; top: 517px; width: 319px; height: 208px; background: var(--white); border: 1px solid #dcdcdc; box-shadow: 0 1px 3px rgba(0,0,0,0.12); padding: 7px; }
  .feature-photo .fill { width: 100%; height: 100%; background: linear-gradient(90deg, #8f93a6 0%, #b9bbc4 40%, #c9483a 70%, #d8c9a8 100%); }

  .site-footer { position: absolute; left: 0; top: 794px; width: 1200px; height: 126px; background: var(--footer-bg); }
  .footer-nav { position: absolute; left: 117px; top: 33px; font-family: "Oxygen", Arial, sans-serif; font-size: 15.5px; color: var(--footer-text); }
  .footer-nav a { color: var(--footer-text); text-decoration: none; }
  .footer-nav .sep { margin: 0 9px; }
  .copyright { position: absolute; left: 117px; top: 65px; font-family: "Open Sans", Arial, sans-serif; font-weight: 300; font-size: 12px; color: var(--footer-muted); }
  .footer-contact { position: absolute; right: 112px; top: 32px; text-align: right; font-family: "Open Sans", Arial, sans-serif; font-size: 12.5px; line-height: 21px; color: var(--footer-text); }
</style>
</head>
<body>
  <header class="site-header">
    <div class="brand">
      <span class="brand-mark"></span>
      <span class="brand-name">VARQOLO</span>
      <span class="brand-divider"></span>
      <span class="brand-tagline">International<br>Merchandise Supply<br>Enterprise</span>
    </div>
    <nav class="main-nav">
      <a href="#" class="is-active">HOME</a>
      <a href="#">ABOUT US</a>
      <a href="#">PRODUCT</a>
      <a href="#">SERVICES</a>
      <a href="#">CONTACT</a>
    </nav>
  </header>

  <section class="hero-band">
    <div class="hero-slide" role="img" aria-label="Close-up photo of a chrome window handle with lock on a soft green background">
      <h2 class="hero-title">International import &amp; export, warehousing<br>and distribution business</h2>
      <div class="slide-dots"><span class="is-current"></span><span></span><span></span><span></span></div>
    </div>
  </section>

  <main class="welcome">
    <h1><span class="light">Welcome to</span> VARQOLO Inc Mainpage</h1>
    <p>VARQOLO Inc is a dynamic, growing international company specialized in offshore sourcing industrial components/parts to help business in North America to reduce overall product/production cost while remain the high quality to meet the market needs. We offer timely, valuable services to source competitive priced products from various top factories in China. Since 2002, we have established branch offices in major cities across North America and China, which facilitate quick communication and cooperation with our suppliers as well as business partners. Headquartered in Toronto, Canada, with two regional offices at mainland China, VARQOLO Inc has established a solid reputation as a reliable partner in bridging the gap between our clients and manufacturers in China. VARQOLO represents a number of manufacturers in China.</p>
  </main>

  <figure class="feature-photo">
    <div class="fill" role="img" aria-label="Warehouse workers in red uniforms moving a shrink-wrapped pallet with a pallet jack"></div>
  </figure>

  <footer class="site-footer">
    <nav class="footer-nav">
      <a href="#">HOME</a><span class="sep">|</span><a href="#">ABOUT US</a><span class="sep">|</span><a href="#">PRODUCT</a><span class="sep">|</span><a href="#">SERVICES</a><span class="sep">|</span><a href="#">CONTACT</a>
    </nav>
    <p class="copyright">Copyright © 2013 Company Name. All rights reserved.</p>
    <address class="footer-contact" style="font-style: normal;">
      4180 Harlow Ave, Suite 300, Markham, ON, L3R 2K9, Canada<br>
      Tel: 416-555-0187, Fax: 416-555-0193
    </address>
  </footer>
</body>
</html>
```